創業130年以上の酢屋です。
国産のりんご果汁だけから造られた「山里の恵み酢」のラベルデザインを依頼します。
一般のスーパーに卸す商品です。たくさん並ぶ大手さんの「りんご酢」に埋もれない、目を引くデザインをお願いしたいです。
容器は瓶で、スタイリッシュなものではなくごく普通の透明な瓶。お酢は薄い琥珀色です(現在のデザインは画像参照)
国産のりんご果汁100%でできているという点がセールスポイントです。
ターゲットは30代以上の女性。
用途はドレッシング作りやマリネなどの料理、フルーツビネガー等のドリンク作りなどです。
「清潔感」「素朴さ」「丁寧な日常」「かわいらしさ」等、30代以上の女性が好むイメージでデザインしてもらいたいです。

縦に並んだりんごのデザインが大変かわいらしく、中央の商品名、その両脇にあるセールスポイントの文言もはっきりと目立っていました。チラッと見ただけでも印象に残り、年配の方でもはっきり読める大きな文字は、20代~50代のどの従業員さんにも好評でした。手に取ってみると、りんごの中に使用方法や弊社の創業年もあり、お客様に伝えた情報がコンパクトにつまっいてる点も採用のポイントとなりました。

初めて利用しましたが、たくさんのデザイナー様にご提案いただき、感激いたしました。
様々なタイプのデザインの中から選ぶことができたので、これまでのモヤモヤ(本当はこれだ!と思ってないけど、選択肢が二択程度しかなくて、どちらかを選ばざるを得ない)が無く、100%納得の決定ができました。
この後、新商品もすぐに出す予定なのでまた利用したいと思っています。
ご応募いただいた皆様、ほんとうにありがとうございました。
またご縁がありましたら、どうぞよろしくお願い致します。
柏原孫右衛門商店(有)
担当:岡部

```html
<!DOCTYPE html>
<html lang="ja">
<head>
<meta charset="utf-8">
<title>山里の恵み酢 ラベル</title>
<link href="https://fonts.googleapis.com/css2?family=Klee+One:wght@600&family=Zen+Maru+Gothic:wght@500&display=swap" rel="stylesheet">
<style>
  :root {
    --page-bg: #f3f2ef;
    --label-bg: #ffffff;
    --apple-red: #c4283a;
    --deep-red: #a51d2e;
    --ink-brown: #7a4a2e;
    --ink-dark: #3b2a20;
  }
  html, body {
    margin: 0;
    padding: 0;
    width: 1200px;
    height: 3340px;
    overflow: hidden;
    background: var(--page-bg);
  }
  .canvas {
    position: relative;
    width: 1200px;
    height: 3340px;
  }
  .label {
    position: absolute;
    left: 0;
    top: 1360px;
    width: 1200px;
    height: 1400px;
    background: var(--label-bg);
    overflow: hidden;
  }
  .band-top {
    position: absolute;
    left: 0; top: 0;
    width: 100%;
    height: 30px;
    background: var(--apple-red);
    border-bottom: 6px solid var(--deep-red);
  }
  .band-bottom {
    position: absolute;
    left: 0; bottom: 0;
    width: 100%;
    height: 130px;
    background: var(--apple-red);
  }
  .band-bottom::before {
    content: "";
    position: absolute;
    left: 0; top: 22px;
    width: 100%;
    height: 6px;
    background: var(--label-bg);
  }
  .claim {
    position: absolute;
    top: 160px;
    width: 100%;
    margin: 0;
    text-align: center;
    font-family: "Klee One", serif;
    font-weight: 600;
    font-size: 84px;
    color: var(--ink-dark);
    letter-spacing: 2px;
  }
  .apple-dots {
    position: absolute;
    top: 370px;
    left: 0;
    width: 100%;
    height: 60px;
  }
  .product-name {
    position: absolute;
    top: 470px;
    width: 100%;
    margin: 0;
    text-align: center;
    font-family: "Klee One", serif;
    font-weight: 600;
    font-size: 172px;
    line-height: 1;
    color: var(--ink-brown);
    letter-spacing: 4px;
  }
  .product-name-en {
    position: absolute;
    top: 730px;
    width: 100%;
    margin: 0;
    text-align: center;
    font-family: "Zen Maru Gothic", sans-serif;
    font-weight: 500;
    font-size: 72px;
    color: var(--ink-dark);
    letter-spacing: 4px;
  }
  .heritage {
    position: absolute;
    top: 940px;
    width: 100%;
    margin: 0;
    text-align: center;
    font-family: "Klee One", serif;
    font-weight: 600;
    font-size: 50px;
    color: var(--ink-dark);
    letter-spacing: 1px;
  }
</style>
</head>
<body>
  <main class="canvas">
    <section class="label" aria-label="山里の恵み酢 ラベル">
      <div class="band-top"></div>
      <p class="claim">国産りんご100%</p>
      <svg class="apple-dots" viewBox="0 0 1200 60" aria-hidden="true">
        <circle cx="484" cy="30" r="26" fill="var(--apple-red)"/>
        <circle cx="600" cy="36" r="26" fill="var(--apple-red)"/>
        <circle cx="716" cy="30" r="26" fill="var(--apple-red)"/>
      </svg>
      <h1 class="product-name">山里の恵み酢</h1>
      <p class="product-name-en">APPLE CIDER VINEGAR</p>
      <p class="heritage">創業130年以上の酢屋が心を込めて作りました</p>
      <div class="band-bottom"></div>
    </section>
  </main>
</body>
</html>
```